Coffeeshop menu for filter tip

We want to have a cannabis (coffeeshop) menu in the size 25mm wide x 60mm wide. Some examples attached.

it must have the following text:
Menu

WEED p/g
Velotrine €16
Cinderfox €14
Tide Rambler €14
Marigolden €16
Grand Pelican €14
Copper Comet €14

HASH p/g
Baltic Ember €12
Harbor Velvet€11
Plum Rova €14
Dusk Maple €10

Target Market(s)

tourist in Amsterdam

Requirements
Nice to have
• cannabis sign leaf
• No Cigarettes allowed symbol

```html
<!DOCTYPE html>
<html lang="en">
<head>
<meta charset="utf-8">
<title>Coffeeshop Filter Tip Menu</title>
<link rel="stylesheet" href="https://fonts.googleapis.com/css2?family=Oswald:wght@500;700&display=swap">
<style>
  :root {
    --red: #d62a2a;
    --orange: #f0a019;
    --green: #1f5a2c;
    --green-deep: #174a22;
    --leaf: #2f8a2e;
    --card: #efe6cf;
    --card-line: #8a6c45;
    --ink: #ffffff;
    --shadow: #1a1a1a;
  }
  html, body {
    margin: 0;
    padding: 0;
    width: 1200px;
    height: 2884px;
    overflow: hidden;
    background: var(--green);
  }
  .menu-strip {
    position: relative;
    width: 1200px;
    height: 2884px;
    overflow: hidden;
    font-family: "Oswald", "Arial Narrow", sans-serif;
  }
  .stripe-field {
    position: absolute;
    inset: 0;
    background:
      linear-gradient(135deg,
        var(--green) 0%, var(--red) 18%, var(--orange) 32%, var(--green) 48%,
        var(--red) 64%, var(--orange) 80%, var(--green) 100%);
  }
  .price-list {
    position: absolute;
    left: 140px;
    right: 122px;
    color: var(--ink);
    font-weight: 700;
    font-style: italic;
    text-shadow: 5px 5px 0 var(--shadow);
    letter-spacing: 2px;
  }
  .price-list .row {
    display: flex;
    justify-content: space-between;
    align-items: center;
  }
  .price-list .heading { letter-spacing: 4px; }
  .weed-list {
    top: 1840px;
    font-size: 112px;
    line-height: 136px;
  }
  .hash-list {
    top: 0;
    height: 470px;
    font-size: 84px;
    line-height: 92px;
    transform: rotate(180deg);
    box-sizing: border-box;
    padding-top: 8px;
  }
  .title-card {
    position: absolute;
    left: 325px;
    top: 773px;
    width: 603px;
    height: 988px;
    background: var(--card);
    box-shadow: 0 0 0 6px rgba(0,0,0,0.08);
  }
  .title-card::before {
    content: "";
    position: absolute;
    inset: 22px;
    border: 5px solid var(--card-line);
  }
  .title-word {
    position: absolute;
    left: 0;
    right: 0;
    text-align: center;
    color: var(--leaf);
    font-weight: 500;
    font-size: 250px;
    line-height: 1;
    letter-spacing: 4px;
  }
  .title-word.top { top: 50px; transform: rotate(180deg); }
  .title-word.bottom { bottom: 50px; }
  .leaf-mark {
    position: absolute;
    left: 60px;
    top: 300px;
    width: 483px;
    height: 390px;
    border-radius: 40%;
    background: radial-gradient(ellipse at center, var(--leaf) 0%, var(--green-deep) 55%, rgba(31,90,44,0) 72%);
  }
</style>
</head>
<body>
<main class="menu-strip">
  <div class="stripe-field" role="img" aria-label="Diagonal chevron stripes in red, orange and green"></div>

  <section class="price-list hash-list" aria-label="Hash prices">
    <div class="row heading"><span>HASH</span><span>p/g</span></div>
    <div class="row"><span>Baltic Ember</span><span>€12</span></div>
    <div class="row"><span>Harbor Velvet</span><span>€11</span></div>
    <div class="row"><span>Plum Rova</span><span>€14</span></div>
    <div class="row"><span>Dusk Maple</span><span>€10</span></div>
  </section>

  <div class="title-card">
    <div class="title-word top">MENU</div>
    <div class="leaf-mark" role="img" aria-label="Green cannabis leaf illustration"></div>
    <h1 class="title-word bottom" style="margin:0">MENU</h1>
  </div>

  <section class="price-list weed-list" aria-label="Weed prices">
    <div class="row heading"><span>WEED</span><span>p/g</span></div>
    <div class="row"><span>Velotrine</span><span>€16</span></div>
    <div class="row"><span>Cinderfox</span><span>€14</span></div>
    <div class="row"><span>Tide Rambler</span><span>€14</span></div>
    <div class="row"><span>Marigolden</span><span>€16</span></div>
    <div class="row"><span>Grand Pelican</span><span>€14</span></div>
    <div class="row"><span>Copper Comet</span><span>€14</span></div>
  </section>
</main>
</body>
</html>
```